We currently have a good logo and we want business cards that can display our logo but also represent our industry - telecom construction - We are a construction company specializing in telecom construction such as installation of fiber optic cable throughout cities and across the country. Nationwide services
We are large enough to handle most any project yet small enough to be a flexible partner and resource.

Target Market(s)

U.S. based telecom carriers and providers

Industry/Entity Type

Construction

Contact Information for Business Card

Business cards should include our logo, phone number and website address. Also, including some information as to our core services would be good.

Colors

Designer to choose colors to be used in the design.

Requirements
Must have
• Colors based on logo
• Must use our logo
• Logo, name, email, website address, phone number
• Tovasco Conduit
• Brent Halvik
• Director of Business Development
• (555) 271-0386
• www.TVSQ-example.com
Nice to have
• Construction services including:
• Small Cell Construction
• Boring/Drilling
• Plowing / Trenching
• Conduit installation
• Fiber pulling
• splicing
• building entries
• Aerial construction
• Aerial Make Ready
• Make Ready Engineering
Should not have
• We are open to ideas

```html
<!DOCTYPE html>
<html lang="en">
<head>
<meta charset="utf-8">
<title>Tovasco Conduit – Business Cards</title>
<link href="https://fonts.googleapis.com/css2?family=Work+Sans:wght@400;500;700&display=swap" rel="stylesheet">
<style>
  :root {
    --bg: #e4e4e4;
    --blue-light: #1ec6f2;
    --blue-mid: #1d8fcf;
    --blue-dark: #0f4c86;
    --brand-blue: #1b6fc4;
    --ink: #3a3a3a;
    --ink-soft: #555;
    --rule: #6a6a6a;
    --white: #ffffff;
  }
  * { margin: 0; padding: 0; box-sizing: border-box; }
  html, body { width: 1200px; height: 930px; overflow: hidden; }
  body {
    background: var(--bg);
    font-family: "Work Sans", Arial, sans-serif;
    position: relative;
  }
  .card {
    position: absolute;
    width: 560px;
    height: 320px;
    border-radius: 22px;
    box-shadow: 0 6px 18px rgba(0,0,0,0.18);
    overflow: hidden;
  }

  /* Front: services */
  .card-front {
    left: 40px; top: 110px;
    background: linear-gradient(35deg, var(--blue-light) 0%, var(--blue-mid) 50%, var(--blue-dark) 100%);
    color: var(--white);
  }
  .card-front .brand {
    position: absolute; top: 78px; left: 0; right: 0;
    text-align: center;
    font-size: 40px; font-weight: 700; letter-spacing: 0.5px;
    color: var(--white);
  }
  .card-front .services {
    position: absolute; top: 190px; left: 20px; right: 20px;
    text-align: center;
    font-size: 15.5px; line-height: 1.55; font-weight: 400;
  }

  /* Back: contact */
  .card-back {
    left: 600px; top: 500px;
    background: var(--white);
    color: var(--ink);
  }
  .card-back .brand {
    position: absolute; top: 62px; left: 34px;
    font-size: 28px; font-weight: 700;
    color: var(--brand-blue);
  }
  .card-back .person {
    position: absolute; top: 100px; right: 34px; width: 300px;
    text-align: right;
  }
  .person .name {
    font-size: 28px; font-weight: 500; letter-spacing: 3px;
    color: var(--brand-blue);
  }
  .person .role {
    font-size: 15px; color: var(--ink-soft);
    padding-bottom: 6px; border-bottom: 1.5px solid var(--rule);
  }
  .person .address {
    margin-top: 22px; font-size: 14.5px; line-height: 1.45; color: var(--ink);
  }
  .card-back .contacts {
    position: absolute; left: 34px; bottom: 30px; width: 330px;
    border-top: 1.5px solid var(--rule);
    padding-top: 10px;
    list-style: none;
    font-size: 16px; line-height: 1.5; color: var(--ink);
  }
  .contacts li { display: flex; align-items: center; gap: 10px; }
  .contacts svg { width: 14px; height: 14px; flex: none; }
  .contacts .accent { color: var(--brand-blue); }
</style>
</head>
<body>

  <section class="card card-front" aria-label="Business card front">
    <div class="brand">Tovasco Conduit</div>
    <p class="services">
      splicing | Fiber pulling | Boring/Drilling | building entries<br>
      Aerial Make Ready | Aerial construction | Conduit installation<br>
      Plowing / Trenching | Small Cell Construction | Make Ready Engineering
    </p>
  </section>

  <section class="card card-back" aria-label="Business card back">
    <div class="brand">Tovasco Conduit</div>

    <div class="person">
      <div class="name">BRENT HALVIK</div>
      <div class="role">Director of Business Development</div>
      <div class="address">48 Larkmoor Street<br>Kansas City, KS 66199</div>
    </div>

    <ul class="contacts">
      <li>
        <svg viewBox="0 0 24 24" aria-hidden="true"><path fill="#444" d="M6.6 10.8a15.1 15.1 0 0 0 6.6 6.6l2.2-2.2a1 1 0 0 1 1-.25 11.4 11.4 0 0 0 3.6.57 1 1 0 0 1 1 1V20a1 1 0 0 1-1 1A17 17 0 0 1 3 4a1 1 0 0 1 1-1h3.5a1 1 0 0 1 1 1c0 1.25.2 2.45.57 3.57a1 1 0 0 1-.25 1z"/></svg>
        (555) 271-0386
      </li>
      <li>
        <svg viewBox="0 0 24 24" aria-hidden="true"><rect x="3" y="5" width="18" height="14" rx="1.5" fill="none" stroke="#444" stroke-width="2"/><path d="M3.5 6l8.5 7 8.5-7" fill="none" stroke="#444" stroke-width="2"/></svg>
        brent.halvik@tovasco-example.com
      </li>
      <li>
        <svg viewBox="0 0 24 24" aria-hidden="true"><circle cx="12" cy="12" r="9" fill="none" stroke="#444" stroke-width="2"/><path d="M3 12h18M12 3c3 3 3 15 0 18M12 3c-3 3-3 15 0 18" fill="none" stroke="#444" stroke-width="1.6"/></svg>
        <span>www.<span class="accent">TVSQ-example</span>.com</span>
      </li>
    </ul>
  </section>

</body>
</html>
```